Yoga Training Cerificate

Design a certificate of graduation from a Vinyasa Yoga Teacher Training Program.

The attached document is an example of the certificate I received as a graduate from a teacher training program. You can use it as a template.

Stylistically, what you design can be: visually enticing, professional, clean, and modern.

Please develop the "Lumen Stretch" logo and embed it within the certificate.

Please add a circular watermark behind the body of the certificate similar to the one found in the attachment; leave out the words Asana Guildhall because I am not associated with that organization.

The name of my school is "Lumen Stretch." And it was established in 2017, which you can include.

The certificate affirms that "' 'such-and-such' has successfully completed the Lumen Stretch modern vinyasa yoga training, completing two hundred hours of instruction in practice and theory. Within the power of our institution as a certifying agent we declare Such-and-such, now, a teacher competent to share the gift of yoga with the masses in a safe and effective."

My name -Dennis Whitcombe- should be at bottom with a faux-signature; position title: Lumen Stretch founder.

If you decide to include text on the fringe, like the example, it might include bars of text describing the maxims of the Lumen Stretch school reading:

This is Lumen Stretch
Breath is primary
Evolve the physical culture
Bring your unique expression to the practice
Take Breaks
Freestyle
Close your eyes
Feel deeper into your body
This is active meditation
This is moving meditation
This is modern meditation

And find a way to integrate Emojis like: Fire, Water, Prayer Hands, etc. as you see fit.

Generally, make the certificate look: official, clear and clean. You can base it from the example given. And try and create a graphic design that is more visually capturing then the example.

```html
<!DOCTYPE html>
<html lang="en">
<head>
<meta charset="utf-8">
<title>Lumen Stretch – Certificate of Completion</title>
<link href="https://fonts.googleapis.com/css2?family=Pinyon+Script&family=Cinzel:wght@500&family=Source+Sans+3:wght@400&family=Crimson+Text:ital@1&family=Alegreya+Sans:wght@400&display=swap" rel="stylesheet">
<style>
  :root {
    --backdrop: #d7ecf7;
    --paper: #ffffff;
    --ink-purple: #4a2a7a;
    --band-purple: #4b2b7d;
    --body-ink: #2e1f5c;
    --bracket: #b1a8f1;
    --gold-light: #f6d27a;
    --gold-dark: #8a5a2a;
    --rule-blue: #7b8fd4;
    --wave-rose: #e7c2cb;
    --wave-rose-deep: #d79aa9;
    --seal: #e6edf2;
  }
  * { margin: 0; padding: 0; box-sizing: border-box; }
  html, body { width: 1200px; height: 1200px; overflow: hidden; background: var(--backdrop); }

  .certificate {
    position: absolute; left: 20px; top: 187px;
    width: 1160px; height: 826px;
    background: var(--paper);
    overflow: hidden;
  }

  .wave-pattern {
    position: absolute; left: 0; top: 0; width: 343px; height: 826px;
    background: linear-gradient(100deg, var(--wave-rose) 0%, #f6e3e8 45%, rgba(255,255,255,0) 100%);
  }

  .gold-frame { position: absolute; left: 0; top: 0; width: 1160px; height: 826px; }

  .maxims {
    position: absolute; left: 75px; top: 200px; width: 303px; height: 426px;
    border: 1px solid #d9a860; border-radius: 12px;
    background: rgba(255,255,255,0.9);
    padding: 20px 0 0 16px;
    font-family: "Source Sans 3", sans-serif; font-size: 16.6px; color: var(--body-ink);
  }
  .maxims li { list-style: none; line-height: 27.7px; }
  .maxims .wrap { max-width: 270px; }

  .school-mark {
    position: absolute; right: 16px; bottom: 20px;
    display: flex; align-items: center; gap: 6px;
    font-family: "Source Sans 3", sans-serif; font-size: 19px; color: #8b2fa0;
  }
  .school-mark .dot { width: 12px; height: 12px; border-radius: 50%; background: #8b2fa0; }

  .title {
    position: absolute; left: 450px; top: 52px; width: 520px; text-align: right;
    font-family: "Pinyon Script", cursive; font-size: 118px; line-height: 1; color: var(--ink-purple);
  }
  .subtitle {
    position: absolute; left: 560px; top: 200px; width: 402px; text-align: right;
    font-family: "Cinzel", serif; font-size: 33px; color: var(--ink-purple); letter-spacing: 1px;
  }

  .affirm-rule { position: absolute; left: 512px; top: 305px; width: 458px; height: 2px; background: var(--rule-blue); }
  .affirm-band {
    position: absolute; left: 593px; top: 291px; width: 295px; height: 28px;
    background: var(--band-purple);
    clip-path: polygon(0 0, 100% 0, 98% 100%, 2% 100%);
    color: #fff; font-family: "Source Sans 3", sans-serif; font-size: 16.5px;
    text-align: center; line-height: 28px;
  }

  .seal { position: absolute; left: 573px; top: 344px; width: 334px; height: 334px; }

  .recipient {
    position: absolute; left: 462px; top: 374px; width: 558px; text-align: center;
    font-family: "Alegreya Sans", sans-serif; font-size: 31px; color: #111;
  }
  .recipient-rule {
    position: absolute; left: 462px; top: 411px; width: 558px; height: 1.5px;
    background: linear-gradient(90deg, rgba(0,0,0,0), #111 15%, #111 85%, rgba(0,0,0,0));
  }

  .statement {
    position: absolute; left: 400px; width: 680px; text-align: center;
    font-family: "Crimson Text", serif; font-style: italic; font-size: 19px; line-height: 23px;
    color: var(--body-ink);
  }
  .statement.first { top: 430px; }
  .statement.second { top: 504px; }

  .signature-rule {
    position: absolute; left: 624px; top: 712px; width: 233px; height: 1.5px;
    background: linear-gradient(90deg, rgba(0,0,0,0), #222 12%, #222 88%, rgba(0,0,0,0));
  }
  .signatory {
    position: absolute; left: 540px; top: 715px; width: 400px; text-align: center;
    font-family: "Cinzel", serif; font-size: 18px; color: var(--body-ink);
  }
  .signatory-role {
    position: absolute; left: 540px; top: 740px; width: 400px; text-align: center;
    font-family: "Crimson Text", serif; font-style: italic; font-size: 16px; color: var(--body-ink);
  }
</style>
</head>
<body>
  <main class="certificate">
    <div class="wave-pattern" role="img" aria-label="Flowing rose line-art wave pattern along the left edge"></div>

    <svg class="gold-frame" viewBox="0 0 1160 826" aria-hidden="true">
      <defs>
        <linearGradient id="goldH" x1="0" x2="1">
          <stop offset="0" stop-color="var(--gold-light)"/>
          <stop offset="0.55" stop-color="#fbe6a8"/>
          <stop offset="1" stop-color="var(--gold-dark)"/>
        </linearGradient>
        <linearGradient id="goldV" x1="0" x2="0" y1="0" y2="1">
          <stop offset="0" stop-color="var(--gold-light)"/>
          <stop offset="1" stop-color="#d9a04a"/>
        </linearGradient>
      </defs>
      <rect x="41" y="40" width="1075" height="2.5" fill="url(#goldH)"/>
      <rect x="41" y="785" width="1075" height="2.5" fill="url(#goldH)"/>
      <rect x="41" y="40" width="2" height="747" fill="url(#goldV)"/>
      <rect x="1114" y="40" width="2" height="747" fill="url(#goldV)"/>
      <g fill="var(--bracket)">
        <path d="M30 29 H97 V52 H53 V99 H30 Z"/>
        <path d="M1130 29 H1063 V52 H1107 V99 H1130 Z"/>
        <path d="M30 797 H97 V774 H53 V727 H30 Z"/>
        <path d="M1130 797 H1063 V774 H1107 V727 H1130 Z"/>
      </g>
    </svg>

    <svg class="seal" viewBox="0 0 334 334" aria-hidden="true">
      <circle cx="167" cy="167" r="160" fill="none" stroke="var(--seal)" stroke-width="12"/>
      <circle cx="167" cy="167" r="128" fill="none" stroke="var(--seal)" stroke-width="3"/>
    </svg>

    <aside class="maxims">
      <ul>
        <li>This is Lumen Stretch</li>
        <li>Breath is primary</li>
        <li>Evolve the physical culture</li>
        <li class="wrap">Bring your unique expression to the practice</li>
        <li>Take Breaks</li>
        <li>Freestyle</li>
        <li>Close your eyes</li>
        <li>Feel deeper into your body</li>
        <li>This is active meditation</li>
        <li>This is moving meditation</li>
        <li>This is modern meditation</li>
      </ul>
      <div class="school-mark"><span class="dot"></span>Lumen Stretch</div>
    </aside>

    <h1 class="title">Certificate</h1>
    <div class="subtitle">of Completion</div>

    <div class="affirm-rule"></div>
    <div class="affirm-band">THE CERTIFICATE AFFIRMS THAT</div>

    <div class="recipient">Name</div>
    <div class="recipient-rule"></div>

    <p class="statement first">has successfully completed the Lumen Stretch modern vinyasa yoga training, completing<br>two hundred hours of instruction in practice and theory.</p>
    <p class="statement second">Within the power of our institution as a certifying agent we declare the person whose<br>name appears above now, a teacher competent to share the gift of yoga with the masses<br>in a safe and effective.</p>

    <div class="signature-rule"></div>
    <div class="signatory">Dennis Whitcombe</div>
    <div class="signatory-role">Lumen Stretch founder.</div>
  </main>
</body>
</html>
```